Infographic for Labor Trends - Supply Chain Theme

Looking to polish this slide up to look professional enough to share with the Board of Directors. The focus is Supply Chain Labor (Warehousing and transportation) Need to have a theme around Supply Chain workforce. Needs to be formatted for wide screen PowerPoint

```html
<!DOCTYPE html>
<html lang="en">
<head>
<meta charset="utf-8">
<title>Supply Chain Job Market Remains Tight</title>
<link rel="stylesheet" href="https://fonts.googleapis.com/css2?family=Open+Sans:wght@400;600;700&family=Carlito:wght@400;700&display=swap">
<style>
  :root {
    --brand-red: #e34b38;
    --banner-red: #e04a36;
    --title-ink: #5b1a10;
    --ink: #333333;
    --muted: #6b6b6b;
    --rule: #d9d9d9;
    --teal: #3f9aa5;
    --teal-dark: #2b6f78;
    --amber: #e3a03b;
    --amber-dark: #a86f1d;
    --red: #d8432f;
    --red-dark: #982a1c;
    --category: #c0368c;
    --line-blue: #2f6fc4;
    --line-pink: #e0508f;
    --line-green: #2e9a7c;
    --line-orange: #e0a545;
    --chart-blue: #3a6fc0;
  }
  * { box-sizing: border-box; margin: 0; padding: 0; }
  html, body { width: 1200px; height: 1200px; overflow: hidden; background: #ffffff; }
  body { position: relative; font-family: "Open Sans", Arial, sans-serif; color: var(--ink); }

  .footer-band { position: absolute; left: 0; top: 887px; width: 1200px; height: 313px; background: var(--brand-red); }

  .title-banner {
    position: absolute; left: 223px; top: 261px; width: 780px; height: 66px;
    background: var(--banner-red);
    box-shadow: 3px 4px 6px rgba(0,0,0,0.35);
    display: flex; align-items: center; justify-content: center;
  }
  .title-banner h1 {
    font-family: "Carlito", "Calibri", sans-serif; font-weight: 700;
    font-size: 35px; color: var(--title-ink); letter-spacing: 0.2px;
  }

  .key-points { position: absolute; left: 104px; top: 349px; width: 506px; }
  .key-point { position: relative; height: 60px; margin-bottom: 14px; display: flex; align-items: center; }
  .key-point svg { position: absolute; left: 0; top: 0; }
  .key-point p {
    margin-left: 66px; width: 440px; height: 46px;
    border: 1px solid #bdbdbd; box-shadow: 1px 2px 3px rgba(0,0,0,0.2);
    padding: 4px 10px 0 10px; font-size: 12.5px; line-height: 16px; color: #3a3a3a;
  }
  .key-point p.small { font-size: 11px; line-height: 14px; padding-top: 2px; }

  .sector-table { position: absolute; left: 117px; top: 580px; width: 510px; }
  .sector-table h2 { text-align: center; font-size: 16.5px; font-weight: 700; color: #2a2a2a; line-height: 20px; }
  .sector-table .subtitle { text-align: center; font-size: 10px; font-weight: 700; color: #2a2a2a; margin-bottom: 5px; }
  .sector-table table { width: 100%; border-collapse: collapse; font-size: 10px; }
  .sector-table th { text-align: left; font-weight: 400; color: var(--chart-blue); font-size: 9px; padding: 1px 4px; border-bottom: 1px solid var(--rule); }
  .sector-table td { padding: 1px 4px; height: 13.5px; border-bottom: 1px solid var(--rule); }
  .sector-table tr.category td { color: var(--category); border-bottom: none; padding-top: 6px; }
  .sector-table td:nth-child(2), .sector-table th:nth-child(2) { width: 140px; }
  .sector-table td:nth-child(3), .sector-table th:nth-child(3) { width: 150px; }

  .postings-chart { position: absolute; left: 627px; top: 353px; }
  .postings-note {
    position: absolute; left: 627px; top: 578px; width: 440px;
    font-size: 9.5px; line-height: 13px; color: #555;
  }
  .incentives-chart { position: absolute; left: 627px; top: 628px; }
  svg text { font-family: "Open Sans", Arial, sans-serif; }
</style>
</head>
<body>
  <div class="title-banner"><h1>Supply Chain Job Market Remains Tight</h1></div>

  <section class="key-points">
    <div class="key-point">
      <svg width="70" height="60" viewBox="0 0 70 60" aria-hidden="true">
        <polygon points="0,30 24,2 66,2 42,30" fill="var(--teal)"/>
        <polygon points="0,30 42,30 66,58 24,58" fill="var(--teal-dark)"/>
      </svg>
      <p>We continue to see pressure and struggle to attract the talent needed to meet staffing demands in multiple markets</p>
    </div>
    <div class="key-point">
      <svg width="70" height="60" viewBox="0 0 70 60" aria-hidden="true">
        <polygon points="0,30 24,2 66,2 42,30" fill="var(--amber)"/>
        <polygon points="0,30 42,30 66,58 24,58" fill="var(--amber-dark)"/>
      </svg>
      <p>Wage inflation in the industry continues and is amplified lack of talent to cover demand for the holiday season cycle</p>
    </div>
    <div class="key-point">
      <svg width="70" height="60" viewBox="0 0 70 60" aria-hidden="true">
        <polygon points="0,30 24,2 66,2 42,30" fill="var(--red)"/>
        <polygon points="0,30 42,30 66,58 24,58" fill="var(--red-dark)"/>
      </svg>
      <p class="small">We expect demand to remain extremely high through 2022 period due to the amount of backlog freight at the ports and missed Holiday placement of goods</p>
    </div>
  </section>

  <section class="sector-table">
    <h2>Some sectors are booming while others lag</h2>
    <div class="subtitle">% change in US job postings, seasonally adjusted, Oct 8 2021</div>
    <table>
      <thead><tr><th>Sectors</th><th>% change since 2/1/20</th><th>% pt change vs 4 weeks ago</th></tr></thead>
      <tbody>
        <tr class="category"><td colspan="3">Better than economy average</td></tr>
        <tr><td>Human Resources</td><td>92.9%</td><td>9.0%</td></tr>
        <tr><td>Production &amp; Manufacturing</td><td>89.9%</td><td>4.1%</td></tr>
        <tr><td>Loading &amp; Stocking</td><td>89.4%</td><td>6.2%</td></tr>
        <tr><td>Pharmacy</td><td>89.0%</td><td>7.5%</td></tr>
        <tr class="category"><td colspan="3">Similar to economy average</td></tr>
        <tr><td>Driving</td><td>51.4%</td><td>7.0%</td></tr>
        <tr><td>Childcare</td><td>50.6%</td><td>6.0%</td></tr>
        <tr><td>Arts &amp; Entertainment</td><td>44.4%</td><td>2.8%</td></tr>
        <tr><td>Food Preparation &amp; Service</td><td>38.7%</td><td>0.7%</td></tr>
        <tr class="category"><td colspan="3">Worse than economy average</td></tr>
        <tr><td>Sales</td><td>20.0%</td><td>1.6%</td></tr>
        <tr><td>Hospitality &amp; Tourism</td><td>18.6%</td><td>2.1%</td></tr>
        <tr><td>Sports</td><td>13.2%</td><td>2.4%</td></tr>
        <tr><td>Beauty &amp; Wellness</td><td>-3.8%</td><td>-3.5%</td></tr>
      </tbody>
    </table>
  </section>

  <svg class="postings-chart" width="440" height="222" viewBox="0 0 440 222" role="img" aria-label="Line chart of job postings by occupational sector">
    <text x="220" y="14" text-anchor="middle" font-size="10.5" font-weight="700" fill="#222">Total Job Postings on HireBoard by Occupational Sector</text>
    <text x="220" y="25" text-anchor="middle" font-size="7.5" font-weight="700" fill="#333">% change in job postings since Feb 1, 2020, seasonally adjusted, to Oct 8, 2021</text>
    <text x="20" y="35" font-size="6" fill="#999">Search for available occupational sectors in the drop-down menu</text>
    <g font-size="7" fill="#333">
      <rect x="20" y="40" width="100" height="12" fill="none" stroke="var(--line-blue)"/><text x="25" y="49">Hospitality &amp; Tourism ×</text>
      <rect x="124" y="40" width="82" height="12" fill="none" stroke="var(--line-pink)"/><text x="129" y="49">Loading &amp; Stocking ×</text>
      <rect x="210" y="40" width="72" height="12" fill="none" stroke="var(--line-green)"/><text x="215" y="49">Logistic Support ×</text>
      <rect x="20" y="56" width="36" height="12" fill="none" stroke="var(--line-orange)"/><text x="25" y="65">Retail ×</text>
    </g>
    <g stroke="#ececec" stroke-width="1">
      <line x1="30" y1="80" x2="425" y2="80"/><line x1="30" y1="100" x2="425" y2="100"/>
      <line x1="30" y1="120" x2="425" y2="120"/><line x1="30" y1="140" x2="425" y2="140"/>
      <line x1="30" y1="160" x2="425" y2="160"/><line x1="30" y1="180" x2="425" y2="180"/>
    </g>
    <g font-size="5.5" fill="#888" text-anchor="end">
      <text x="27" y="82">100%</text><text x="27" y="102">50%</text><text x="27" y="122">25%</text>
      <text x="27" y="142">0%</text><text x="27" y="162">-25%</text><text x="27" y="182">-50%</text>
    </g>
    <g fill="none" stroke-width="1.4">
      <polyline stroke="var(--line-orange)" points="32,140 45,142 58,156 70,160 85,152 100,145 130,140 160,138 190,134 220,128 250,120 280,112 310,106 340,100 370,98 400,96 422,94"/>
      <polyline stroke="var(--line-pink)" points="32,140 45,141 58,152 70,155 85,146 100,136 130,130 160,126 190,120 220,112 250,104 280,98 310,92 340,88 370,84 400,82 422,78"/>
      <polyline stroke="var(--line-green)" points="32,140 45,143 58,162 70,168 85,160 100,156 130,152 160,150 190,146 220,140 250,132 280,122 310,112 340,104 370,98 400,92 422,88"/>
      <polyline stroke="var(--line-blue)" points="32,140 45,145 58,170 70,178 85,174 100,170 130,168 160,166 190,164 220,160 250,152 280,140 310,130 340,126 370,120 400,118 422,114"/>
    </g>
    <g font-size="5" fill="#888">
      <text x="32" y="198">Feb 20</text><text x="95" y="198">Jun 20</text><text x="160" y="198">Oct 20</text>
      <text x="225" y="198">Feb 21</text><text x="290" y="198">Jun 21</text><text x="395" y="198">Oct 21</text>
    </g>
    <rect x="432" y="0" width="7" height="205" fill="#e6e6e6"/>
    <rect x="433" y="4" width="5" height="170" fill="#bdbdbd"/>
  </svg>

  <p class="postings-note">Job postings on HireBoard are a real-time measure of labour market activity. On July 16, 2021, they were 36.5% above February 1, 2020, the pre-pandemic baseline, after adjusting for seasonal variation. However, job postings increased in May, June, and July at a slower pace than in March and April.</p>

  <svg class="incentives-chart" width="440" height="225" viewBox="0 0 440 225" role="img" aria-label="Line chart of share of postings advertising hiring incentives">
    <text x="220" y="14" text-anchor="middle" font-size="13" font-weight="700" fill="#222">More postings are advertising hiring incentives</text>
    <text x="220" y="28" text-anchor="middle" font-size="9" fill="#333">Share of job postings that advertise hiring incentives through July 16, 2021</text>
    <g stroke="#ededed"><line x1="20" y1="45" x2="425" y2="45"/><line x1="20" y1="75" x2="425" y2="75"/><line x1="20" y1="105" x2="425" y2="105"/><line x1="20" y1="135" x2="425" y2="135"/><line x1="20" y1="165" x2="425" y2="165"/></g>
    <line x1="20" y1="195" x2="425" y2="195" stroke="#999"/>
    <g font-size="8" fill="#555" text-anchor="end">
      <text x="14" y="48">5%</text><text x="14" y="78">4%</text><text x="14" y="108">3%</text>
      <text x="14" y="138">2%</text><text x="14" y="168">1%</text><text x="14" y="198">0%</text>
    </g>
    <polyline fill="none" stroke="var(--chart-blue)" stroke-width="1.8" points="22,142 40,140 60,137 80,136 100,133 120,129 140,124 150,122 160,127 180,128 200,127 220,126 240,124 260,122 280,119 300,112 320,104 340,96 360,88 380,80 395,71 410,68 420,68"/>
    <g font-size="8" fill="#444" text-anchor="middle">
      <text x="22" y="212">Jul 2020</text><text x="120" y="212">Oct 2020</text><text x="218" y="212">Jan 2021</text>
      <text x="316" y="212">Apr 2021</text><text x="410" y="212">Jul 2021</text>
    </g>
  </svg>

  <div class="footer-band"></div>
</body>
</html>
```